Web Design For Metal Recycling Company

We are a scrap and recycling company dealing mainly in scrap metal base in Singapore. We deal in both domestic market and international market. Currently we are still unsure if we want to have a "lively" or "professional" company image so we will leave it to the designer to deem what is good.

We wish for a website to be able to "Retain" the interest of new visitor and at the same time able to give enough information for new and existing customer. We would also wish for design that will get the visitor to "Engage" us.

The attached is the logo for the company and we would want to incorporate that into the website. Either of the logo is fine.

```html
<!DOCTYPE html>
<html lang="en">
<head>
<meta charset="utf-8">
<title>Pellivar Recycling</title>
<link href="https://fonts.googleapis.com/css2?family=Audiowide&family=Open+Sans:wght@400;600;700&display=swap" rel="stylesheet">
<style>
:root{
  --gold:#c9961a;
  --gold-light:#e0b23a;
  --beige:#e8d5a9;
  --dark:#1e1a17;
  --text-grey:#7a7a7a;
  --field:#e6e6e6;
  --white:#ffffff;
  --display:'Audiowide', sans-serif;
  --body:'Open Sans', sans-serif;
}
*{margin:0;padding:0;box-sizing:border-box}
html,body{width:1200px;height:1029px;overflow:hidden;background:var(--white)}
body{position:relative;font-family:var(--body)}
.hero{position:absolute;left:0;top:0;width:1200px;height:379px;border-top:4px solid var(--gold);
  background:radial-gradient(ellipse at 55% 60%,#f0a060 0%,#c8582a 35%,#7a2a12 70%,#3a1508 100%);}
.hero-photo{position:absolute;inset:0}
.header-bar{position:absolute;left:0;top:0;width:1200px;height:89px;background:rgba(40,30,25,.35)}
.brand{position:absolute;left:172px;top:17px;display:flex;align-items:center;gap:12px}
.brand-square{width:52px;height:52px;background:var(--white);border:3px solid var(--gold)}
.brand-name{font-family:var(--body);font-weight:600;color:var(--white);font-size:26px;letter-spacing:.5px;white-space:nowrap}
.support{position:absolute;right:173px;top:16px;color:var(--white);font-family:var(--display);text-align:right}
.support span{display:block;font-size:9px;line-height:11px}
.support strong{font-size:14px;font-weight:400;line-height:16px}
.support-icon{position:absolute;left:-30px;top:1px}
.nav{position:absolute;left:669px;top:48px;width:361px;height:35px;display:flex;background:rgba(255,255,255,.12)}
.nav a{font-family:var(--display);font-size:9px;color:rgba(255,255,255,.55);text-decoration:none;padding:12px 12px 0;white-space:nowrap}
.nav a.active{color:var(--white);border-bottom:2px solid var(--white)}
.hero-text{position:absolute;left:150px;top:188px;width:900px;text-align:center;font-family:var(--display);color:var(--white);font-size:18px;line-height:23.5px;text-transform:uppercase;text-shadow:0 1px 3px rgba(0,0,0,.6);white-space:nowrap}
.arrow{position:absolute;top:203px;width:50px;height:50px;border-radius:50%;background:rgba(255,255,255,.3)}
.arrow.prev{left:105px}.arrow.next{left:1045px}
.arrow svg{position:absolute;left:16px;top:13px}
.dots{position:absolute;left:573px;top:312px;display:flex;gap:3px}
.dots i{width:6px;height:6px;background:rgba(255,255,255,.5)}
.dots i.on{background:var(--gold);width:8px;height:8px;margin-top:-1px}
.welcome{position:absolute;top:379px;left:0;width:1200px;height:192px;text-align:center}
.section-title{font-family:var(--display);font-weight:400;color:var(--gold);font-size:15px;line-height:18px}
.welcome .section-title{margin-top:45px}
.welcome p{color:var(--text-grey);font-size:14px;line-height:16.5px;width:800px;margin:15px auto 0;white-space:nowrap}
.services{position:absolute;top:571px;left:0;width:1200px;height:184px;background:var(--beige);box-shadow:0 8px 10px -6px rgba(0,0,0,.35)}
.card{position:absolute;top:29px;width:265px;height:129px;overflow:hidden}
.card-photo{position:absolute;inset:0}
.card-panel{position:absolute;left:0;top:0;width:137px;height:100%;background:rgba(20,16,14,.6);padding:18px 0 0 15px}
.card h3{font-family:var(--display);font-weight:400;color:var(--white);font-size:15px;line-height:18px}
.card p{color:var(--white);font-size:10.5px;line-height:13.5px;margin-top:4px;width:122px;white-space:nowrap}
.card .more{display:inline-flex;margin-top:4px;font-size:8px;font-weight:700;background:var(--white);color:var(--dark)}
.card .more span{padding:3px 8px}
.card .more b{border-left:1px solid #ccc;padding:2px 5px}
.card.featured{border:2px solid var(--gold);box-shadow:0 0 10px rgba(0,0,0,.5)}
.card.featured h3,.card.featured p{color:var(--gold-light)}
.card.featured .more{background:var(--gold);color:var(--white)}
.card.featured .more b{border-color:#e8c060}
.footer-col{position:absolute;top:796px}
.field{width:273px;background:var(--field);color:#8a8a8a;font-size:11px;padding:9px 12px;margin-top:5px;height:31px}
.send{position:absolute;left:182px;top:160px;width:91px;height:24px;background:var(--gold);display:flex;color:var(--white);font-size:11px;font-weight:700}
.send span{flex:1;text-align:center;line-height:24px}
.send b{width:26px;border-left:1px solid #e0b850;text-align:center;line-height:24px}
.map{width:272px;height:153px;border:3px solid var(--gold-light);margin-top:14px;background:linear-gradient(135deg,#ece9e2,#dedbd3)}
.footer-brand{display:flex;align-items:center;gap:8px;margin-top:30px}
.footer-brand .brand-square{width:30px;height:30px;border-width:2px}
.footer-brand .brand-name{font-size:17px;color:var(--gold)}
.copyright{font-size:10.5px;color:#777;width:240px;margin-top:8px;line-height:14px}
.social{display:flex;gap:18px;margin-top:14px}
.social i{width:32px;height:32px;background:#999;border-radius:3px}
.social i.s1{background:#3c5a99}.social i.s3{background:#333}
</style>
</head>
<body>
<header class="hero">
  <div class="hero-photo" role="img" aria-label="Photo of coiled copper scrap wire"></div>
  <div class="header-bar"></div>
  <div class="brand"><div class="brand-square"></div><div class="brand-name">Pellivar Recycling</div></div>
  <div class="support">
    <svg class="support-icon" width="20" height="22" viewBox="0 0 20 22"><circle cx="10" cy="6" r="5" fill="#fff"/><path d="M1 22c0-7 4-9 9-9s9 2 9 9z" fill="#fff"/></svg>
    <span>CUSTOMER SUPPORT</span><strong>+ 0022 11 44 33 66</strong>
  </div>
  <nav class="nav"><a class="active">HOME</a><a>ABOUT US</a><a>PRODUCT &amp; SERVICES</a><a>CONTACT US</a></nav>
  <p class="hero-text">Pellivar, your one stop solution to all your scrap ferrous,<br>non-ferrous and other recyclable.<br>With more than 30 years of experience in the industry, we know<br>your needs.</p>
  <div class="arrow prev"><svg width="18" height="24"><path d="M14 2 4 12l10 10" stroke="#fff" stroke-width="2" fill="none"/></svg></div>
  <div class="arrow next"><svg width="18" height="24"><path d="M4 2l10 10-10 10" stroke="#fff" stroke-width="2" fill="none"/></svg></div>
  <div class="dots"><i></i><i></i><i></i><i class="on"></i><i></i><i></i></div>
</header>

<section class="welcome">
  <h2 class="section-title">WELCOME</h2>
  <p>Pellivar Hardware provides a one stop solution for procurement, recycling and trading of ferrous and<br>non-ferrous scrap metal products for industries and individual.</p>
  <p>Pellivar Hardware was first established in 1981 as “Pellivar Lead Dealer” to provide the service of recycling<br>of ferrous and non-ferrous scrap metal for the local market.</p>
</section>

<section class="services">
  <article class="card" style="left:192px">
    <div class="card-photo" role="img" aria-label="Photo of tangled copper scrap" style="background:linear-gradient(120deg,#3a2418,#8a5030 50%,#2a1a12)"></div>
    <div class="card-panel"><h3>SCRAP</h3><p>Duis autem vel eum<br>iriure dolor in hendrerit<br>in vulputate...</p><a class="more"><span>Read More</span><b>+</b></a></div>
  </article>
  <article class="card featured" style="left:468px;top:30px;width:263px;height:128px">
    <div class="card-photo" role="img" aria-label="Photo of cut copper cable ends" style="background:linear-gradient(120deg,#1a1a1a,#4a4440 50%,#222)"></div>
    <div class="card-panel" style="padding-top:20px"><h3>RECYCLING</h3><p>Lorem ipsum dolor sit<br>amet, consectetuer<br>adipiscing eli...</p><a class="more"><span>Read More</span><b>+</b></a></div>
  </article>
  <article class="card" style="left:742px;width:264px;height:128px">
    <div class="card-photo" role="img" aria-label="Photo of a recycling bin" style="background:linear-gradient(120deg,#2a2826,#55504a 60%,#8a8884)"></div>
    <div class="card-panel" style="padding-top:21px"><h3>CONTACT</h3><p>Ut wisi enim ad minim<br>veniam, quis nostrud<br>exerci tation ..</p><a class="more"><span>Read More</span><b>+</b></a></div>
  </article>
</section>

<footer>
  <div class="footer-col" style="left:172px;width:273px">
    <h2 class="section-title">CONTACT FORM</h2>
    <div style="margin-top:8px">
      <div class="field">Name*</div>
      <div class="field">Email*</div>
      <div class="field" style="height:58px">Message*</div>
    </div>
    <div class="send"><span>SEND</span><b>&gt;</b></div>
  </div>
  <div class="footer-col" style="left:468px">
    <h2 class="section-title">MAP</h2>
    <div class="map" role="img" aria-label="Street map showing the company location"></div>
  </div>
  <div class="footer-col" style="left:761px">
    <div class="footer-brand"><div class="brand-square"></div><div class="brand-name">Pellivar Recycling</div></div>
    <p class="copyright">© Copyright 2014 Pellivar Hardware. All rights reserved.</p>
    <div class="social"><i class="s1" aria-label="Social link"></i><i aria-label="Social link"></i><i class="s3" aria-label="Social link"></i><i aria-label="Social link"></i></div>
  </div>
</footer>
</body>
</html>
```